Global Weight loss program

we need a business card based in Brooklyn , NY called PeppertonRUN . Mara Dulvik Tenbrook the founder and creator of PeppertonRUN Movement. A business based around nutrition, health, Whole Foods and fitness.

Industry/Entity Type

Food Service

Contact Information for Business Card

Phone number : 718-555-0143
website www.peppertonrun.com
email : mara@peppertonrun.com

Font styles to use
Sans Serif

Requirements
Must have
• logo colors
• green black and gold
Nice to have
• must be simple and sharp.
Should not have
• pictures of items

```html
<!DOCTYPE html>
<html lang="en">
<head>
<meta charset="UTF-8">
<title>PeppertonRUN Business Card</title>
<link href="https://fonts.googleapis.com/css2?family=Open+Sans:wght@400;600;700&display=swap" rel="stylesheet">
<style>
  :root {
    --page-bg: #e9e7e2;
    --card-white: #ffffff;
    --ink-dark: #2b2b2b;
    --ink-grey: #555555;
    --brand-green: #5fae2a;
    --brand-green-light: #8cc63f;
    --card-shadow: rgba(0, 0, 0, 0.18);
  }
  * { margin: 0; padding: 0; box-sizing: border-box; }
  html, body {
    width: 1200px;
    height: 840px;
    overflow: hidden;
  }
  body {
    background: var(--page-bg);
    font-family: "Open Sans", Arial, sans-serif;
    position: relative;
  }
  .card {
    position: absolute;
    top: 105px;
    width: 360px;
    height: 630px;
    background: var(--card-white);
    box-shadow: 0 10px 30px var(--card-shadow);
    overflow: hidden;
  }
  .card--front { left: 200px; }
  .card--back { left: 640px; }

  /* Front */
  .front-brand {
    position: absolute;
    top: 170px;
    left: 0;
    right: 0;
    display: flex;
    flex-direction: column;
    align-items: center;
  }
  .brand-mark {
    width: 22px;
    height: 22px;
    background: var(--brand-green);
    margin-bottom: 18px;
  }
  .brand-name {
    font-size: 38px;
    font-weight: 700;
    letter-spacing: -1px;
    color: var(--ink-dark);
    line-height: 1;
  }
  .brand-tagline {
    margin-top: 6px;
    font-size: 12px;
    letter-spacing: 1.5px;
    color: var(--ink-grey);
  }
  .role-band {
    position: absolute;
    left: 0;
    right: 0;
    bottom: 0;
    height: 175px;
    background: linear-gradient(90deg, var(--brand-green-light), var(--brand-green));
    display: flex;
    flex-direction: column;
    justify-content: center;
    padding: 0 34px;
    color: var(--card-white);
    font-size: 15px;
    line-height: 1.6;
  }

  /* Back */
  .back-brand {
    position: absolute;
    top: 60px;
    right: 34px;
    text-align: right;
  }
  .back-brand .brand-name { font-size: 34px; }
  .back-brand .brand-tagline { font-size: 11px; }
  .contact {
    position: absolute;
    left: 40px;
    top: 260px;
  }
  .person-name {
    font-size: 20px;
    font-weight: 700;
    color: var(--brand-green);
    text-transform: uppercase;
    letter-spacing: 0.5px;
  }
  .person-title {
    font-size: 14px;
    color: var(--ink-dark);
    text-transform: uppercase;
    margin-bottom: 16px;
  }
  .contact-label {
    font-size: 13px;
    font-weight: 700;
    color: var(--brand-green);
    text-transform: uppercase;
    margin-top: 10px;
  }
  .contact-value {
    font-size: 15px;
    color: var(--ink-grey);
    text-transform: uppercase;
  }
</style>
</head>
<body>
  <section class="card card--front">
    <div class="front-brand">
      <div class="brand-mark"></div>
      <div class="brand-name">PeppertonRUN</div>
      <div class="brand-tagline">Fitness, Nutrition and Health</div>
    </div>
    <div class="role-band">
      <p>Health Coach | Personal Trainer</p>
      <p>Natural Gourmet Chef</p>
    </div>
  </section>

  <section class="card card--back">
    <div class="back-brand">
      <div class="brand-name">PeppertonRUN</div>
      <div class="brand-tagline">Fitness, Nutrition and Health</div>
    </div>
    <div class="contact">
      <p class="person-name">Mara Dulvik Tenbrook</p>
      <p class="person-title">Founder</p>
      <p class="contact-label">Phone</p>
      <p class="contact-value">718-555-0143</p>
      <p class="contact-label">Email</p>
      <p class="contact-value">mara@peppertonrun.com</p>
      <p class="contact-label">Web</p>
      <p class="contact-value">www.peppertonrun.com</p>
    </div>
  </section>
</body>
</html>
```